"Oral Surgery Office needs a Business Card Design with Logo"

We need a logo design and business card. The name of the office is Tassingford Oral Surgery & Implant Center. The final design should communicate uniqueness as well as highly class office. The business card should emphasize power. I included the current business card below. Please design something unique

Target Market(s)

Dentists & Patients

Industry/Entity Type

Dental

Contact Information for Business Card

Unique Design to show success, prestige, Style, unmatched performance

Font styles to use
Serif

Colors
1b1b1b
ffffff
0556a4

Requirements
Must have
• Bussiness Name, Doctor's Name, Website, phone and Fax, email, office address
• Color should be either Black and White or Blue and White
Nice to have
• Clean look
Should not have
• the business card shouldn't be too busy. I feel like the old business card was too busy

```html
<!DOCTYPE html>
<html lang="en">
<head>
<meta charset="utf-8">
<title>Tassingford Oral Surgery &amp; Implant Center – Business Card</title>
<link rel="stylesheet" href="https://fonts.googleapis.com/css2?family=Lato:wght@300;400;700&display=swap">
<style>
  :root {
    --brand-blue: #0556a4;
    --card-white: #f3f3f1;
    --ink-white: #ffffff;
    --ink-muted: #5673a6;
    --backdrop: #dadada;
  }
  * { margin: 0; padding: 0; box-sizing: border-box; }
  html, body { width: 1200px; height: 1200px; overflow: hidden; }
  body {
    background: var(--backdrop);
    font-family: "Lato", Arial, sans-serif;
    display: flex;
    flex-direction: column;
    align-items: center;
    justify-content: center;
    gap: 70px;
  }
  .card {
    width: 840px;
    height: 480px;
    position: relative;
    box-shadow: 0 6px 18px rgba(0,0,0,0.12);
  }
  /* Front */
  .card-front {
    background: var(--brand-blue);
    color: var(--ink-white);
    display: flex;
    flex-direction: column;
    align-items: center;
    justify-content: center;
    gap: 26px;
  }
  .brand-mark {
    border-radius: 50%;
    border: 2px solid currentColor;
  }
  .card-front .brand-mark { width: 150px; height: 150px; }
  .brand-name {
    font-weight: 700;
    text-align: center;
    line-height: 1.2;
  }
  .card-front .brand-name { font-size: 36px; }
  /* Back */
  .card-back {
    background: var(--card-white);
    color: var(--brand-blue);
  }
  .back-brand {
    position: absolute;
    left: 70px;
    top: 60px;
    display: flex;
    align-items: center;
    gap: 24px;
  }
  .card-back .brand-mark { width: 100px; height: 100px; }
  .card-back .brand-name { font-size: 26px; text-align: left; }
  .contact-block {
    position: absolute;
    left: 420px;
    top: 230px;
  }
  .doctor-name { font-size: 24px; font-weight: 700; }
  .doctor-title { font-size: 19px; font-weight: 300; color: var(--ink-muted); margin-bottom: 18px; }
  .contact-list { list-style: none; }
  .contact-list li {
    display: flex;
    align-items: flex-start;
    gap: 12px;
    font-size: 18px;
    line-height: 1.45;
    color: var(--ink-muted);
  }
  .contact-list svg { width: 16px; height: 16px; margin-top: 5px; flex: none; fill: var(--brand-blue); }
</style>
</head>
<body>
  <section class="card card-front">
    <div class="brand-mark"></div>
    <p class="brand-name">Tassingford Oral Surgery<br>&amp; Implant Center</p>
  </section>

  <section class="card card-back">
    <div class="back-brand">
      <div class="brand-mark"></div>
      <p class="brand-name">Tassingford Oral Surgery<br>&amp; Implant Center</p>
    </div>
    <div class="contact-block">
      <p class="doctor-name">Marcus Ellery</p>
      <p class="doctor-title">Dental Specialist</p>
      <ul class="contact-list">
        <li><svg viewBox="0 0 16 16"><path d="M3 1l3 3-1.5 2c1 2 3 4 5 5L11.5 9.5l3 3-2 2.5C7 14 2 9 1 3z"/></svg>+0198-765432</li>
        <li><svg viewBox="0 0 16 16"><path d="M4 1h6l2 2v3H4zM1 7h14v6h-3v2H4v-2H1zM5 11v3h6v-3z"/></svg>+0198-765432</li>
        <li><svg viewBox="0 0 16 16"><path d="M15 1L1 7l5 2 1 6 3-4 4 2z"/></svg>info@tassingfordoral.com</li>
        <li><svg viewBox="0 0 16 16"><path d="M8 1a7 7 0 100 14A7 7 0 008 1zm0 1.5c.9 0 1.8 1.8 2 4.5H6c.2-2.7 1.1-4.5 2-4.5zM2.6 7h2.2c.1-1.6.4-3 .9-3.9A5.5 5.5 0 002.6 7zm8.6 0h2.2a5.5 5.5 0 00-3.1-3.9c.5.9.8 2.3.9 3.9zM2.6 9a5.5 5.5 0 003.1 3.9c-.5-.9-.8-2.3-.9-3.9zm3.4 0c.2 2.7 1.1 4.5 2 4.5s1.8-1.8 2-4.5zm5.2 0c-.1 1.6-.4 3-.9 3.9A5.5 5.5 0 0013.4 9z"/></svg>www.tassingfordoral.com</li>
        <li><svg viewBox="0 0 16 16"><path d="M8 1l7 6.5h-2V15H9.5v-4h-3v4H3V7.5H1z"/></svg>48 Harlow Lane,<br>Tassingford</li>
      </ul>
    </div>
  </section>
</body>
</html>
```